Yoga class opening. Little schedule for JUNE JULY and AUGUST

Flyer to promote an opening yoga class. The color of the docx haven't to be respected.

We want something joyfull, professional, clean and serious.

About the logo we oppened a contest at the same time so at the moment there is no logo but the logo color will be simple.

The phone number will change so you can poste a random one for the design that i can change by myself.

i recieved many creation in both side BUT i want something in 1 side :)

Yoga student. all age

It Professional

Yoga brook

Sans Serif

• The text present on the docx
• Some symbols about yoga ( Namasté signs, mandala, ... )
• Not too much details it has to be clear.

```html
<!DOCTYPE html>
<html lang="fr">
<head>
<meta charset="utf-8">
<title>Yoga Brook – Stages et ateliers d'été</title>
<link href="https://fonts.googleapis.com/css2?family=Alegreya:ital,wght@0,500;1,500;1,700&family=PT+Sans:wght@400;700&family=Oswald:wght@500&display=swap" rel="stylesheet">
<style>
  :root{
    --page:#efe9e3;
    --paper:#ffffff;
    --orange:#f48c4c;
    --orange-text:#f08a4b;
    --blue:#36a7dc;
    --ink:#3a3a3a;
    --grey-text:#555555;
    --logo-grey:#8e8f92;
    --rule:#c9c9c9;
    --social:#3b5a98;
    --headline-font:'Alegreya', Georgia, serif;
    --body-font:'PT Sans', Arial, sans-serif;
    --display-font:'Oswald', 'Arial Narrow', sans-serif;
  }
  *{box-sizing:border-box;margin:0;padding:0}
  html,body{width:1200px;height:1000px;overflow:hidden;background:var(--page)}
  .flyer{position:absolute;left:282px;top:50px;width:636px;height:900px;background:var(--paper);box-shadow:0 4px 14px rgba(0,0,0,.18);font-family:var(--body-font);color:var(--ink)}
  .abs{position:absolute}
  .hero-photo{left:0;top:0;width:636px;height:272px;background:linear-gradient(100deg,#d9dde3 0%,#eef0f3 35%,#f7f8fa 60%,#e4e7ec 100%)}
  .logo-slot{left:478px;top:18px;width:122px;height:56px;background:var(--logo-grey);color:#fff;font:700 14px var(--body-font);display:flex;align-items:center;justify-content:center}
  .title-card{left:283px;top:87px;width:317px;height:150px;background:rgba(255,255,255,.94);box-shadow:0 3px 8px rgba(0,0,0,.25);text-align:center}
  .title-card .kicker{margin-top:18px;font:700 20px var(--body-font);letter-spacing:5px;color:var(--grey-text)}
  .title-card .studio{margin-top:6px;font:500 26px/30px var(--headline-font);letter-spacing:2.5px;color:var(--orange-text);text-transform:uppercase}
  .title-card .address{margin-top:8px;font:400 10px var(--body-font);letter-spacing:1.2px;color:var(--grey-text)}
  .band{left:0;top:272px;width:636px;height:72px;background:var(--orange);color:#fff;text-align:center;font:italic 700 17px/22px var(--headline-font);letter-spacing:.8px;padding-top:13px}
  .month-tag{width:110px;height:24px;border-radius:12px;background:var(--blue);color:#fff;font:italic 700 19px/24px var(--headline-font);text-align:center;box-shadow:3px 3px 3px rgba(0,0,0,.12)}
  .offer-title{font:italic 700 17px/20px var(--headline-font);color:var(--orange-text)}
  .price{font:400 17px var(--body-font);color:var(--ink)}
  .slots{list-style:none;font:400 8px/15px var(--body-font);color:var(--ink)}
  .rule{left:30px;width:576px;height:1px;background:var(--rule)}
  .season-start{font:700 10px var(--body-font);color:var(--ink)}
  .social-square{width:38px;height:39px;background:var(--social)}
  .contact{font:700 12px/15px Arial, var(--body-font), sans-serif;color:var(--ink)}
  .contact .lead{color:var(--social);font-weight:400}
  .farewell{font:500 27px var(--display-font);letter-spacing:3px;color:var(--orange)}
</style>
</head>
<body>
<main class="flyer">
  <div class="abs hero-photo" role="img" aria-label="Photo d'une femme en posture de méditation sur un tapis dans un studio lumineux"></div>
  <div class="abs logo-slot">Your logo</div>
  <div class="abs title-card">
    <p class="kicker">NOUVEAU!!</p>
    <h1 class="studio">Votre studio<br>de yoga a Ixelles</h1>
    <p class="address">212 CHAUSSÉE DE VERLAINE 1050 IXELLES</p>
  </div>
  <div class="abs band">En attendant le planning des cours de la rentrée,<br>YOGA BROOK vous propose ses stages et ateliers d’été.</div>

  <!-- Juin -->
  <div class="abs month-tag" style="left:36px;top:364px">JUIN</div>
  <h2 class="abs offer-title" style="left:45px;top:405px">Stage découverte du YOGA</h2>
  <p class="abs price" style="left:45px;top:427px">10h00 85 €</p>
  <ul class="abs slots" style="left:45px;top:456px">
    <li>Du lundi 6 au vendredi 10 juin : 10h00 à 12h00 ou 18h00 à 20h00</li>
    <li>Du lundi 13 au vendredi 17 juin : 10h00 à 12h00 ou 18h00 à 20h00</li>
    <li>Du lundi 20 au vendredi 24 juin : 10h00 à 12h00 ou 18h00 à 20h00</li>
    <li>Du lundi 27 au vendredi 1er juillet : 10h00 à 12h00 ou 18h00 à 20h00</li>
  </ul>
  <h2 class="abs offer-title" style="left:347px;top:386px">Atelier gestion du stress yoga/<br>sophrologie</h2>
  <p class="abs price" style="left:347px;top:428px">2h00 28 €</p>
  <ul class="abs slots" style="left:347px;top:457px">
    <li>Samedi 11 juin 10h30 à 12h30</li>
    <li>Samedi 11 juin 15h à 17h00</li>
    <li>Dimanche 12 juin 10h30 à 12h30</li>
    <li>Dimanche 12 juin 14h à 16h00</li>
  </ul>
  <div class="abs rule" style="top:537px"></div>

  <!-- Juillet -->
  <div class="abs month-tag" style="left:39px;top:556px">JUILLET</div>
  <h2 class="abs offer-title" style="left:45px;top:594px">Stage initiation à l’ASHTANGA</h2>
  <p class="abs price" style="left:45px;top:615px">10h00 85 €</p>
  <ul class="abs slots" style="left:45px;top:645px">
    <li>Du lundi 4 au vendredi 8 juillet : 10h00 à 12h00 ou 18h00 à 20h00</li>
    <li>Du lundi 11 au vendredi 15 juillet : 10h00 à 12h00 ou 18h00 à 20h00</li>
    <li>Du lundi 18 au vendredi 22 juillet : 10h00 à 12h00 ou 18h00 à 20h00</li>
    <li>Du lundi 25 au vendredi 29 juillet : 10h00 à 12h00 ou 18h00 à 20h00</li>
  </ul>
  <h2 class="abs offer-title" style="left:347px;top:576px">Atelier gestion du stress yoga/<br>sophrologie</h2>
  <p class="abs price" style="left:347px;top:618px">2h00 28 €</p>
  <ul class="abs slots" style="left:347px;top:647px">
    <li>Samedi 9 juillet 10h30 à 12h30</li>
    <li>Samedi 9 juillet 15h00 à 17h00</li>
    <li>Dimanche 10 juillet 10h30 à 12h30</li>
    <li>Dimanche 10 juillet 14h00 à 16h00</li>
  </ul>
  <div class="abs rule" style="top:718px"></div>

  <!-- Août -->
  <div class="abs month-tag" style="left:39px;top:735px">AOUT</div>
  <h2 class="abs offer-title" style="left:45px;top:764px">Stage découverte du YOGA</h2>
  <p class="abs price" style="left:45px;top:786px">10h00 85 €</p>
  <ul class="abs slots" style="left:45px;top:816px">
    <li>Du lundi 1er au vendredi 5 août : 10h00 à 12h00 ou 18h00 à 20h00</li>
    <li>Du lundi 8 au vendredi 12 août : 10h00 à 12h00 ou 18h00 à 20h00</li>
    <li>Du lundi 15 au vendredi 19 août : 10h00 à 12h00 ou 18h00 à 20h00</li>
    <li>Du lundi 22 au vendredi 26 août : 10h00 à 12h00 ou 18h00 à 20h00</li>
  </ul>

  <p class="abs season-start" style="left:347px;top:740px">Démarrage du planning annuel le 5 septembre 2016</p>
  <div class="abs social-square" style="left:348px;top:767px"></div>
  <p class="abs contact" style="left:395px;top:765px">
    <span class="lead">Plus d’info et inscription :</span><br>
    Ou via notre page friendspace :<br>
    www.friendspace.com/yogabrook
  </p>
  <p class="abs farewell" style="left:343px;top:822px">UN BEL ETE A TOUS !</p>
</main>
</body>
</html>
```